A Quiet Harvest Book Cover Design

I require a book cover design to be completed for my book "A Quiet Harvest" How to build a highly profitable sports store!

This is my third attempt at engaging a graphic designer for this project. My last attempt was a terrible experience and ended up costing me more than double my original budget.

The successful designer will be engaged for more monthly jobs as they come to hand which would be brochure designs, web graphics etc.

I'm initially looking for this cover to drive online engagement, and sell this manuscript on Lumora with the vision to later roll out a hard copy in 6-12 months time.

My business is called The Fennick Crew - I'm a retail expert consultant who specialises in advanced shop floor retail solutions. I've worked with some of Australia's largest sporting goods retailers and have trained over 5000 employees. My goal is to inspire retail standards to greater levels, and continue helping to this industry employ millions of people around the world. I'm known for inspiring my clients to pivot their retail approach to more sustainable and long term strategies.

Please find attached a design brief.

Any questions, please ask upfront.

*important* all designers read the design brief thoroughly.

```html
<!DOCTYPE html>
<html lang="en">
<head>
<meta charset="utf-8">
<title>A Quiet Harvest – Back Cover</title>
<link href="https://fonts.googleapis.com/css2?family=Roboto+Condensed:wght@700&family=Oswald:wght@500&display=swap" rel="stylesheet">
<style>
  :root {
    --cover-grey: #b4b5b8;
    --ink: #231f20;
    --accent-pink: #e3198c;
    --rule-white: #ffffff;
    --photo-light: #c9a58a;
    --photo-dark: #3b3530;
  }
  html, body {
    margin: 0;
    padding: 0;
    overflow: hidden;
  }
  body {
    width: 927px;
    height: 1200px;
    background: var(--cover-grey);
  }
  .back-cover {
    position: relative;
    width: 927px;
    height: 1200px;
    background: var(--cover-grey);
    color: var(--ink);
    font-family: "Roboto Condensed", "Arial Narrow", sans-serif;
    font-weight: 700;
    font-size: 16px;
    line-height: 21.3px;
    overflow: hidden;
  }
  .blurb-column {
    position: absolute;
    top: 50px;
    width: 400px;
  }
  .blurb-column p {
    margin: 0 0 21.3px;
  }
  .blurb-left { left: 53px; }
  .blurb-right { left: 476px; }
  .drop-cap {
    float: left;
    color: var(--accent-pink);
    font-size: 66px;
    line-height: 44px;
    margin: 4px 3px 0 0;
    padding-top: 4px;
  }
  .learn-list {
    list-style: none;
    margin: 0 0 21.3px;
    padding: 0;
  }
  .learn-list li {
    padding-left: 16px;
    text-indent: -10px;
  }
  .learn-list li::before {
    content: "•";
    display: inline-block;
    width: 10px;
    text-indent: 0;
  }
  .learn-list .tight { letter-spacing: -0.5px; }
  .double-rule {
    position: absolute;
    left: 56px;
    width: 817px;
    height: 18px;
  }
  .rule-top { top: 560px; }
  .rule-bottom { top: 742px; }
  .endorsement {
    position: absolute;
    top: 590px;
    left: 100px;
    width: 740px;
    margin: 0;
    font-size: 16.4px;
    line-height: 21.5px;
  }
  .about-heading {
    position: absolute;
    top: 806px;
    left: 56px;
    margin: 0;
    font-size: 14.5px;
  }
  .author-photo {
    position: absolute;
    top: 860px;
    left: 56px;
    width: 151px;
    height: 196px;
    background: linear-gradient(160deg, var(--photo-light) 0%, #a88468 45%, var(--photo-dark) 100%);
  }
  .author-bio {
    position: absolute;
    top: 862px;
    left: 224px;
    width: 640px;
    font-size: 16.4px;
    line-height: 21.5px;
  }
  .author-bio p { margin: 0 0 21.5px; }
  .site-line {
    position: absolute;
    top: 1083px;
    left: 0;
    width: 927px;
    margin: 0;
    text-align: center;
    font-family: "Oswald", "Roboto Condensed", sans-serif;
    font-weight: 500;
    font-size: 31px;
    letter-spacing: 0.2px;
  }
</style>
</head>
<body>
<main class="back-cover">

  <section class="blurb-column blurb-left">
    <p><span class="drop-cap">W</span>anted to live the dream of owning a sports store but you're NOW LIVING A REAL LIFE NIGHTMARE?</p>
    <p>Do you know sports better than most people, but can't seem to transition that knowledge to help your sports store grow?</p>
    <p>You most likely have frustrations around a lack of LOYAL customers, you find it really hard to attract and keep quality staff, and, you're struggling with online pricing?</p>
    <p>A QUIET HARVEST is the book for all you ex sporting greats and experts who love working with sports &amp; leisure people, but haven't unlocked how to use it to pay the bills and run a PROFITABLE SPORTS STORE.</p>
    <p>Written specifically for people who have limited</p>
  </section>

  <section class="blurb-column blurb-right">
    <p>retail knowledge but are experts or professionals inside a sporting field, A QUIET HARVEST dulls down the noise and bright shiny lights, and places a set of working priorities in front of you to follow and profit from.</p>
    <p style="margin-bottom:0">Inside you'll learn:</p>
    <ul class="learn-list">
      <li>How to ensure you're solving your sporting clients problems effectively</li>
      <li>Which retail method is right for your store</li>
      <li>How to manage your inventory effectively</li>
      <li>The best way to market a sports store</li>
      <li>How to recruit and build an INVINCIBLE team, and</li>
      <li class="tight">How to deliver remarkable experiences for you clients</li>
    </ul>
    <p>If you want more customers, dollars, profits and ultimately time through your sports store then read and uncover the 7 step PREMIER retail method that unlocks MORE CUSTOMERS, MORE PROFITS, and MORE TIME.</p>
  </section>

  <svg class="double-rule rule-top" viewBox="0 0 817 18" aria-hidden="true">
    <rect x="0" y="0" width="817" height="6" fill="var(--rule-white)"/>
    <rect x="0" y="12" width="817" height="3" fill="var(--rule-white)"/>
  </svg>

  <blockquote class="endorsement">“Many ex pat sporting greats slap a chunk of money down, open a sports store in a small town and expect the tills to ring... Doesn't work that way anymore. Customers need more than just a good price. A QUIET HARVEST absolutely helps retail owners and franchisees focus on the important retail aspects and clearly shows how to manage a retail business to greater results, it's a retail life saver” - Dale Prescott - Director of Crewline</blockquote>

  <svg class="double-rule rule-bottom" viewBox="0 0 817 18" aria-hidden="true">
    <rect x="0" y="0" width="817" height="3" fill="var(--rule-white)"/>
    <rect x="0" y="9" width="817" height="6" fill="var(--rule-white)"/>
  </svg>

  <h2 class="about-heading">About the Author</h2>
  <div class="author-photo" role="img" aria-label="Head-and-shoulders portrait photograph of the author"></div>
  <section class="author-bio">
    <p>Marcus Dunleavy is a retail thought leader and sports retailing specialist. His business The Fennick Crew has advised and consulted to some of Australia's leading sporting goods retailers including Ridgeway, Coastline Athletics, and Summit Wheel Co.</p>
    <p>Marcus specialises in working with retail teams on sales and selling strategies, retail team recruitment and training, instore layout and visual executions, database &amp; loyalty marketing structures.</p>
  </section>

  <p class="site-line">Visit&nbsp; for more www.aquietharvest.com.au</p>

</main>
</body>
</html>
```